Tactical Supply Company needing memorable business card design

Our tactical supply comapny is in need of a new business card design that will set us apart from the amateurs. We sell tactical gear ranging from backpacks and range bags to apparel and other gear. We are looking for a sharp design that incorporates our logo, website, and name. Our colors are white, red, and black, or any combination of the three, preferably red and black.
I have attached our logo with our name underneath but I have also edited that design with the logo incorporated next to the name (attached).

Target Market(s)

Law enforcement, military, tactical

Industry/Entity Type

Business

Contact Information for Business Card

Include www.fernhollowprovisions-demo.com

Colors
000000
ec1f27
ffffff

Requirements
Must have
• Our name, logo, and website. This is intended to be a memorable simple card, no name, address, email, or phone number info is necessary. Designs that do include this additional info will still be considered if they are absolutely spectacular.
Should not have
• A standard template design, I can create that in my own on Cardvellum. I am looking for a new, creative design that is completely unique to my company.

```html
<!DOCTYPE html>
<html lang="en">
<head>
<meta charset="utf-8">
<title>Fernhollow Provisions – Business Card</title>
<link rel="stylesheet" href="https://fonts.googleapis.com/css2?family=Open+Sans:wght@400;600;700;800&display=swap">
<style>
  :root {
    --ink: #000000;
    --red: #ec1f27;
    --paper: #ffffff;
    --grey: #3a3a3a;
    --stage: #e9e7e3;
  }
  html, body {
    margin: 0;
    width: 1200px;
    height: 885px;
    overflow: hidden;
    background: var(--stage);
    font-family: "Open Sans", Arial, sans-serif;
  }
  .canvas {
    width: 1200px;
    height: 885px;
    display: flex;
    align-items: center;
    justify-content: center;
    gap: 40px;
  }
  .card {
    width: 540px;
    height: 309px;
    border-radius: 16px;
    position: relative;
    box-sizing: border-box;
    box-shadow: 0 6px 18px rgba(0,0,0,.18);
    overflow: hidden;
  }
  /* Front */
  .card--front { background: var(--paper); color: var(--grey); }
  .brand {
    display: flex;
    align-items: center;
    gap: 10px;
  }
  .brand__mark {
    width: 16px;
    height: 16px;
    background: var(--red);
  }
  .brand__name {
    font-weight: 800;
    text-transform: uppercase;
    line-height: 1.05;
    letter-spacing: .5px;
  }
  .card--front .brand {
    position: absolute;
    left: 34px;
    top: 40px;
  }
  .card--front .brand__name { color: var(--red); font-size: 24px; }
  .person {
    position: absolute;
    right: 34px;
    top: 42px;
    text-align: right;
  }
  .person__name { color: var(--red); font-weight: 700; font-size: 22px; margin: 0; }
  .person__role { font-size: 12px; margin: 2px 0 0; color: var(--grey); }
  .divider {
    position: absolute;
    left: 34px;
    right: 34px;
    top: 122px;
    height: 1px;
    background: var(--ink);
  }
  .contacts {
    position: absolute;
    left: 34px;
    bottom: 30px;
    margin: 0;
    padding: 0;
    list-style: none;
    font-size: 12.5px;
  }
  .contacts li {
    display: flex;
    align-items: center;
    gap: 9px;
    margin-top: 6px;
  }
  .contacts__icon {
    width: 15px;
    height: 15px;
    border-radius: 3px;
    background: var(--red);
    flex: none;
  }
  .address {
    position: absolute;
    right: 34px;
    top: 140px;
    text-align: right;
    font-size: 12.5px;
    line-height: 1.5;
    margin: 0;
  }
  /* Back */
  .card--back {
    background: var(--ink);
    color: var(--paper);
    display: flex;
    flex-direction: column;
    align-items: center;
    justify-content: center;
    gap: 26px;
  }
  .card--back .brand__name { color: var(--paper); font-size: 28px; text-align: left; }
  .card--back .brand__mark { width: 20px; height: 20px; }
  .website {
    display: flex;
    align-items: center;
    gap: 14px;
    font-weight: 700;
    font-size: 15px;
  }
  .website__rule { width: 70px; height: 2px; background: var(--red); }
</style>
</head>
<body>
  <main class="canvas">
    <section class="card card--front" aria-label="Card front">
      <div class="brand">
        <span class="brand__mark"></span>
        <span class="brand__name">Fernhollow<br>Provisions</span>
      </div>
      <div class="person">
        <p class="person__name">Employee Name</p>
        <p class="person__role">Managing Director</p>
      </div>
      <div class="divider"></div>
      <p class="address">Millbrook, Ohio<br>44019</p>
      <ul class="contacts">
        <li><span class="contacts__icon"></span>hello@fernhollowprovisions-demo.com</li>
        <li><span class="contacts__icon"></span>social.example/fernhollowprovisions</li>
        <li><span class="contacts__icon"></span>posts.example/fernhollowprov</li>
        <li><span class="contacts__icon"></span>photos.example/fernhollowprovisions/</li>
      </ul>
    </section>

    <section class="card card--back" aria-label="Card back">
      <div class="brand">
        <span class="brand__mark"></span>
        <span class="brand__name">Fernhollow<br>Provisions</span>
      </div>
      <div class="website">
        <span class="website__rule"></span>
        <span>www.fernhollowprovisions-demo.com</span>
        <span class="website__rule"></span>
      </div>
    </section>
  </main>
</body>
</html>
```